Business IT Services Billboard to attract local small businesses

We are Brivolane, a premier Managed Service Provider (MSP) specializing in comprehensive IT services and VOIP phone solutions exclusively for businesses. Our goal is to create a dynamic and visually engaging billboard advertisement that not only highlights our cutting-edge IT solutions but also emphasizes our state-of-the-art VOIP phone services. This billboard should communicate our commitment to providing innovative, reliable, and holistic technology solutions.
Target Market(s)
small business
Industry/Entity Type
Information Technology
Colors
Designer to choose colors to be used in the design.
Look and feel
Each slider illustrates characteristics of the customer's brand and the style your logo design should communicate.

```html
<!DOCTYPE html>
<html lang="en">
<head>
<meta charset="utf-8">
<title>Brivolane — Next-Gen IT and VOIP Services Billboard</title>
<link rel="stylesheet" href="https://fonts.googleapis.com/css2?family=Exo+2:ital,wght@0,600;0,700;0,800;1,500;1,600&display=swap">
<style>
  :root {
    --backdrop: #2a2a2a;
    --brand-blue: #1d6db3;
    --navy: #1c3f6e;
    --white: #ffffff;
    --panel-light: #f3f5f7;
    --panel-mid: #dfe4ea;
    --subtitle: #e3eefa;
    --logo-blue: #1d6db3;
  }
  * { margin: 0; padding: 0; box-sizing: border-box; }
  html, body {
    width: 853px; height: 1200px; overflow: hidden;
    background: var(--backdrop);
    font-family: "Exo 2", sans-serif;
  }
  .billboard {
    position: absolute; left: 56px; top: 765px;
    width: 742px; height: 210px;
    background: linear-gradient(135deg, var(--panel-light), var(--panel-mid));
    overflow: hidden;
  }
  .billboard > * { position: absolute; white-space: nowrap; }
  .billboard__skyline {
    right: 0; top: 0; width: 300px; height: 210px;
    background: linear-gradient(180deg, rgba(200,208,218,0.55), rgba(240,243,246,0));
  }
  .billboard__blue { left: 0; top: 0; width: 470px; height: 210px; }
  .tagline-label {
    left: 30px; top: 8px;
    background: var(--white); color: var(--navy);
    font-weight: 800; font-size: 18px; line-height: 26px;
    padding: 0 10px; border-radius: 2px;
  }
  .headline-it {
    left: 30px; top: 34px;
    color: var(--white); font-weight: 800; font-size: 52px; line-height: 52px;
    letter-spacing: -0.5px;
  }
  .headline-and {
    left: 22px; top: 122px; width: 44px; text-align: center;
    color: var(--white); font-weight: 700; font-size: 22px; line-height: 24px;
    transform: rotate(-90deg);
  }
  .headline-voip {
    left: 62px; top: 84px;
    color: var(--white); font-weight: 800; font-size: 88px; line-height: 88px;
    letter-spacing: -1px;
  }
  .headline-services {
    left: 262px; top: 144px;
    color: var(--white); font-weight: 700; font-size: 21px; line-height: 24px;
  }
  .subtitle {
    left: 32px; top: 172px;
    color: var(--subtitle); font-style: italic; font-weight: 600;
    font-size: 14px; line-height: 16px;
  }
  .brand-name {
    left: 444px; top: 6px; width: 280px; text-align: center;
    color: var(--logo-blue); font-weight: 800; font-size: 32px; line-height: 40px;
    letter-spacing: 1px;
  }
  .phone-visual {
    left: 500px; top: 50px; width: 150px; height: 92px;
    background: linear-gradient(160deg, #4a4f57, #23262b);
    border-radius: 8px;
  }
  .cta-label {
    left: 482px; top: 146px; width: 212px;
    background: var(--brand-blue); color: var(--white);
    font-style: italic; font-weight: 600; font-size: 12px; line-height: 18px;
    text-align: center;
  }
  .cta-url {
    left: 482px; top: 168px; width: 212px; text-align: center;
    color: var(--navy); font-weight: 600; font-size: 21px; line-height: 28px;
  }
</style>
</head>
<body>
  <section class="billboard" aria-label="Brivolane billboard">
    <div class="billboard__skyline" role="img" aria-label="Faint city office buildings in the background"></div>
    <svg class="billboard__blue" viewBox="0 0 470 210" aria-hidden="true">
      <defs>
        <linearGradient id="blueField" x1="0" y1="0" x2="1" y2="1">
          <stop offset="0" stop-color="#2179c4"/>
          <stop offset="1" stop-color="#15589a"/>
        </linearGradient>
      </defs>
      <polygon points="0,0 470,0 428,210 0,210" fill="url(#blueField)"/>
    </svg>

    <div class="tagline-label">Boost Your Business with</div>
    <h1 class="headline-it">Next-Gen IT</h1>
    <span class="headline-and">and</span>
    <span class="headline-voip">VOIP</span>
    <span class="headline-services">Services</span>
    <p class="subtitle">Seamless Technology Solutions Tailored<br>for Your Business Success</p>

    <div class="brand-name">BRIVOLANE</div>
    <div class="phone-visual" role="img" aria-label="Office VOIP desk phone with touchscreen"></div>
    <div class="cta-label">Transform Your Tech Today at</div>
    <div class="cta-url">www.brivolane.com</div>
  </section>
</body>
</html>
```